Web page design for food business

The website is pantryloop.com.au and is an ordering website with thumbnails for purchasing high quality delicatessen products + fruit & vegetables.
The site is simple with a focus on clicking foods to buy and then pay for. There are no complicated product reviews or anything. Aside from the normal about us and contact us pages the website is essentially thumbnails for ordering and a high quality homepage to educate and showcase the business when people go to the URL.
There are 2 main tasks
The first task is a page design (i.e. header, footer, sides...) to carry through for all the pages in the website.
The second task is for the homepage specifically. I want a professional looking homepage with 3 large slide banners that look "elegant" and "artisan" as this is a deli website not a general grocery website. One slider should refer to "daily deliveries" and I will leave the other 2 sliders to your professional judgement. The homepage should also provide for room under the slide banner for specials/products of the month/etc and general promotional information
Target Market(s)
higher income earners, foodies, professionals, quality foods
Industry/Entity Type
Food Store
Number of Pages Required
2 page
Requirements
Must have
- Fresh quality food ready to be delivered
- Ease of ordering
- The feel of a high quality deli
Nice to have
- References to fresh fruit and vegetables for greenery and freshness
Should not have
- .

```html
<!DOCTYPE html>
<html lang="en">
<head>
<meta charset="utf-8">
<title>pantryloop.com.au – Free Delivery</title>
<link href="https://fonts.googleapis.com/css2?family=Open+Sans:wght@400;600;700&display=swap" rel="stylesheet">
<style>
:root{
  --orange:#f7941d;
  --orange-dark:#e9780c;
  --green:#8cc63f;
  --green-dark:#6fa82a;
  --ink:#333333;
  --muted:#8a8a8a;
  --line:#e2e2e2;
  --panel:#f4f4f4;
  --footer:#1f1f1f;
  --footer-deep:#141414;
  --white:#ffffff;
}
*{box-sizing:border-box;margin:0;padding:0}
html,body{width:716px;height:1200px;overflow:hidden}
body{font-family:"Open Sans",Arial,sans-serif;color:var(--ink);background:var(--white);position:relative;font-size:8px}
.wrap{width:490px;margin:0 auto;position:relative}

/* header */
.site-header{height:62px}
.brand{position:absolute;left:0;top:14px}
.brand-name{font-size:20px;font-weight:700;color:var(--ink);letter-spacing:-.3px;line-height:1}
.brand-tag{font-size:8px;color:var(--ink);margin-top:4px}
.account-links{position:absolute;right:0;top:8px;display:flex;gap:6px;font-size:6.5px;color:var(--muted);align-items:center}
.search{position:absolute;right:0;top:36px;width:112px;height:13px;border:1px solid var(--line);font-size:6px;color:#aaa;padding:2px 5px}
.search svg{position:absolute;right:3px;top:2px}

/* nav */
.main-nav{height:20px;background:linear-gradient(var(--orange),var(--orange-dark))}
.main-nav ul{list-style:none;display:flex;height:20px;align-items:center;width:490px;margin:0 auto}
.main-nav li{color:var(--white);font-size:6.5px;font-weight:700;padding:0 10px;line-height:20px;border-right:1px solid rgba(255,255,255,.35)}
.main-nav li.active{background:rgba(0,0,0,.08)}

/* hero */
.hero{height:222px;background:linear-gradient(#f7f7f7,#ffffff);border-bottom:1px solid var(--line)}
.hero .wrap{height:222px}
.hero-copy{position:absolute;left:0;top:58px;width:220px}
.hero-title{font-size:21px;font-weight:400;color:var(--orange);letter-spacing:.5px}
.hero-sub{font-size:9px;color:var(--green-dark);margin-top:4px}
.hero-text{font-size:6px;color:var(--muted);margin-top:4px;line-height:1.5}
.btn{display:inline-block;background:var(--green);color:var(--white);font-weight:600;border-radius:2px}
.hero .btn{font-size:6.5px;padding:4px 11px;margin-top:8px}
.dots{position:absolute;left:0;top:163px;display:flex;gap:4px}
.dots span{width:6px;height:6px;border-radius:50%;background:#999}
.dots span:first-child{background:#555}
.hero-photo{position:absolute;right:12px;top:26px;width:190px;height:160px;border-radius:4px;background:radial-gradient(ellipse at 50% 30%,#e84a2c 0,#f2a02a 30%,#7bb23a 55%,#b4823f 75%,#f7f7f7 100%)}

/* intro */
.intro{text-align:center;padding-top:52px}
.intro h1{font-size:17px;font-weight:400;color:#444}
.intro p{font-size:9px;color:#666;margin-top:3px}

/* shop area */
.shop{position:absolute;top:432px;left:113px;width:490px;height:330px}
.sidebar{position:absolute;left:0;top:0;width:125px}
.cat-box{border:1px solid var(--line);background:var(--white)}
.cat-box h3{font-size:7.5px;font-weight:600;background:var(--panel);padding:6px 8px;border-bottom:1px solid var(--line)}
.cat-box ul{list-style:none;padding:5px 8px}
.cat-box li{font-size:6.3px;color:#555;line-height:13px;display:flex;align-items:center;gap:5px}
.cat-box li::before{content:"";width:5px;height:5px;border:1px solid #bbb}
.offer{margin-top:10px;background:var(--orange);color:var(--white);text-align:center;padding:9px 8px 10px}
.offer h4{font-size:9px;font-weight:700}
.offer p{font-size:5.5px;line-height:1.5;margin-top:3px}
.offer .btn-outline{display:inline-block;border:1px solid var(--white);font-size:6px;padding:3px 9px;margin-top:6px}

.featured{position:absolute;left:137px;top:0;width:353px}
.featured h2{font-size:10.5px;color:var(--orange);font-weight:600;margin:-2px 0 8px}
.grid-3{display:grid;grid-template-columns:repeat(3,1fr);gap:9px}
.card{border:1px solid var(--line);background:var(--white);padding:5px}
.card .photo{height:68px;border-radius:2px}
.card .name{font-size:6.5px;font-weight:600;margin-top:5px}
.card .desc{font-size:5px;color:var(--muted);margin-top:1px}
.card .buy{display:flex;justify-content:space-between;align-items:center;margin-top:5px}
.price{font-size:7.5px;font-weight:700;color:var(--orange)}
.card .btn{font-size:5.5px;padding:2px 6px}

/* month */
.month{position:absolute;top:790px;left:0;width:716px;height:248px;background:var(--panel);border-top:1px solid var(--line)}
.month-title{display:flex;align-items:center;justify-content:center;gap:10px;margin-top:24px}
.month-title h2{font-size:15px;font-weight:400;color:#444}
.month-title i{display:block;width:55px;height:1px;background:#bbb}
.grid-4{display:grid;grid-template-columns:repeat(4,1fr);gap:10px;margin-top:20px}
.grid-4 .photo{height:82px}

/* footer */
.site-footer{position:absolute;top:1038px;left:0;width:716px;height:162px;background:var(--footer);color:#bbb}
.foot-cols{display:flex;gap:22px;padding-top:18px}
.foot-col h5{font-size:7.5px;color:var(--white);font-weight:700;margin-bottom:5px}
.foot-col li{list-style:none;font-size:5.8px;line-height:10px}
.foot-col{width:70px}
.newsletter{width:170px;margin-left:14px}
.newsletter p{font-size:5.8px;line-height:1.5}
.newsletter .field{height:13px;background:var(--white);margin-top:6px;width:130px;font-size:5.5px;color:#999;padding:3px 5px}
.newsletter .btn{font-size:6px;padding:3px 9px;margin-top:6px}
.foot-bar{position:absolute;bottom:0;left:0;width:716px;height:28px;background:var(--footer-deep)}
.foot-bar .wrap{display:flex;justify-content:space-between;align-items:center;height:28px;font-size:5.5px}
.social{display:flex;gap:4px}
.social span{width:10px;height:10px;background:#555;border-radius:2px}
</style>
</head>
<body>

<header class="site-header">
  <div class="wrap">
    <div class="brand">
      <div class="brand-name">pantryloop.com.au</div>
      <div class="brand-tag">Free Delivery</div>
    </div>
    <div class="account-links">
      <span>My Account</span><span>|</span><span>Login</span><span>|</span><span>Sign Up</span><span>|</span><span>Checkout</span>
      <svg width="10" height="9" viewBox="0 0 10 9"><path d="M0 1h2l1.3 5h5L10 2.5H3" fill="none" stroke="#555" stroke-width="1"/><circle cx="4" cy="8" r=".9" fill="#555"/><circle cx="8" cy="8" r=".9" fill="#555"/></svg>
    </div>
    <div class="search">Search
      <svg width="8" height="8" viewBox="0 0 8 8"><circle cx="3.2" cy="3.2" r="2.3" fill="none" stroke="#888"/><path d="M5 5l2.5 2.5" stroke="#888"/></svg>
    </div>
  </div>
</header>

<nav class="main-nav">
  <ul>
    <li class="active">HOME</li><li>ABOUT US</li><li>OUR PRODUCTS</li><li>CATEGORY</li><li>BEST SELLERS</li><li>ORDER NOW</li><li>CONTACT</li>
  </ul>
</nav>

<section class="hero">
  <div class="wrap">
    <div class="hero-copy">
      <h2 class="hero-title">DAILY DELIVERIES</h2>
      <p class="hero-sub">Class aptent taciti sociosqu ad litora torquent</p>
      <p class="hero-text">Fresh produce and fine deli goods picked each morning and brought straight to your door.</p>
      <span class="btn">Read More</span>
    </div>
    <div class="dots"><span></span><span></span><span></span><span></span></div>
    <div class="hero-photo" role="img" aria-label="Wooden crate filled with fresh fruit and vegetables"></div>
  </div>
</section>

<section class="intro">
  <h1>Fresh quality food ready to be delivered</h1>
  <p>Praesent sit amet est dictum dolor eu dictum porttitor</p>
</section>

<section class="shop">
  <aside class="sidebar">
    <div class="cat-box">
      <h3>Product Category</h3>
      <ul>
        <li>Cheeses</li><li>Confectionery</li><li>Dips, Spreads</li><li>Fresh Bread</li><li>Fruit</li><li>Herbs</li><li>Nuts &amp; Seeds</li><li>Oil &amp; Vinegars</li><li>Olives, Antipasto</li><li>Pickles</li><li>Salt &amp; Seasonings</li>
      </ul>
    </div>
    <div class="offer">
      <h4>Special Offers</h4>
      <p>Seasonal deli picks at member prices,<br>updated every single week.</p>
      <span class="btn-outline">View More</span>
    </div>
  </aside>

  <div class="featured">
    <h2>Featured Products</h2>
    <div class="grid-3">
      <div class="card"><div class="photo" role="img" aria-label="Fresh ginger root" style="background:radial-gradient(#c9a068,#f3ece2)"></div><div class="name">Product Name</div><div class="desc">Fresh and hand selected daily</div><div class="buy"><span class="price">$17.58</span><span class="btn">Add to Cart</span></div></div>
      <div class="card"><div class="photo" role="img" aria-label="Pomegranates" style="background:radial-gradient(#b3202a,#f6e4e2)"></div><div class="name">Product Name</div><div class="desc">Fresh and hand selected daily</div><div class="buy"><span class="price">$17.58</span><span class="btn">Add to Cart</span></div></div>
      <div class="card"><div class="photo" role="img" aria-label="Mandarins with leaves" style="background:radial-gradient(#f08a1c,#f8ead6)"></div><div class="name">Product Name</div><div class="desc">Fresh and hand selected daily</div><div class="buy"><span class="price">$17.58</span><span class="btn">Add to Cart</span></div></div>
      <div class="card"><div class="photo" role="img" aria-label="Dried pasta" style="background:radial-gradient(#f0c441,#fbf3d9)"></div><div class="name">Product Name</div><div class="desc">Fresh and hand selected daily</div><div class="buy"><span class="price">$17.58</span><span class="btn">Add to Cart</span></div></div>
      <div class="card"><div class="photo" role="img" aria-label="Bottle of olive oil" style="background:radial-gradient(#9c8a1e,#f3f0dc)"></div><div class="name">Product Name</div><div class="desc">Fresh and hand selected daily</div><div class="buy"><span class="price">$17.58</span><span class="btn">Add to Cart</span></div></div>
      <div class="card"><div class="photo" role="img" aria-label="Medjool dates" style="background:radial-gradient(#7a3a1c,#f1e3da)"></div><div class="name">Product Name</div><div class="desc">Fresh and hand selected daily</div><div class="buy"><span class="price">$17.58</span><span class="btn">Add to Cart</span></div></div>
    </div>
  </div>
</section>

<section class="month">
  <div class="month-title"><i></i><h2>Special Product of the Month</h2><i></i></div>
  <div class="wrap grid-4">
    <div class="card"><div class="photo" role="img" aria-label="Carrots" style="background:radial-gradient(#ee7a22,#fbe9da)"></div><div class="name">Product Name</div><div class="desc">Locally grown this season</div><div class="buy"><span class="price">$17.58</span><span class="btn">Add to Cart</span></div></div>
    <div class="card"><div class="photo" role="img" aria-label="Potatoes" style="background:radial-gradient(#a7774a,#f3e9df)"></div><div class="name">Product Name</div><div class="desc">Locally grown this season</div><div class="buy"><span class="price">$17.58</span><span class="btn">Add to Cart</span></div></div>
    <div class="card"><div class="photo" role="img" aria-label="Pineapple" style="background:radial-gradient(#d9a52b,#6f9a3a 60%,#f3f3ea)"></div><div class="name">Product Name</div><div class="desc">Locally grown this season</div><div class="buy"><span class="price">$17.58</span><span class="btn">Add to Cart</span></div></div>
    <div class="card"><div class="photo" role="img" aria-label="Halved kiwifruit" style="background:radial-gradient(#8cbf3a,#eef5e1)"></div><div class="name">Product Name</div><div class="desc">Locally grown this season</div><div class="buy"><span class="price">$17.58</span><span class="btn">Add to Cart</span></div></div>
  </div>
</section>

<footer class="site-footer">
  <div class="wrap foot-cols">
    <div class="foot-col"><h5>COMPANY</h5><ul><li>About Us</li><li>Why Us</li><li>Careers</li><li>Testimonials</li><li>Store Settings</li></ul></div>
    <div class="foot-col"><h5>PRODUCTS</h5><ul><li>Shipping and Delivery</li><li>Payment Methods</li><li>Specials</li><li>Events</li><li>Help</li></ul></div>
    <div class="foot-col"><h5>SUPPORT</h5><ul><li>FAQs</li><li>Privacy Policy</li><li>Recommendations</li><li>Contact</li></ul></div>
    <div class="foot-col newsletter"><h5>NEWSLETTER SIGN UP</h5><p>Get weekly specials and new arrivals sent to your inbox.</p><div class="field">Email Address</div><span class="btn">SUBSCRIBE</span></div>
  </div>
  <div class="foot-bar">
    <div class="wrap"><span>© 2015 Company Name. All rights reserved. Terms of Use</span><div class="social"><span></span><span></span><span></span></div></div>
  </div>
</footer>

</body>
</html>
```